Roofing Company needs YOU to help put us on top!

Brindlecrest Roofing, a fresh new company with quality and Innovation in mind, needs your help to stand out in the competitive Chicago market. With over 30 years of experience, all the right people and tools for the job, the only thing we are missing is your creative ideas in web design to help us grow our online presence.
Our Company offers exceptional quality at reasonable prices, we work for the everyday people both blue collar and white collar.

We have used MakerHarbor in the past with multiple successful campaigns, we are excited to see what you can come up with for our website.

www.BrindlecrestRoofing-demo.net will be the domain

We will be hiring a photographer for visual content on our pages later. Stock photos are okay to use but should follow theme.

Thank you for taking the time on the submissions, if you have any questions don't hesitate to ask and we will provide whatever is needed to you.

Target Market(s)

Homeowners & Commercial Clients between 21-65

Industry/Entity Type

Roofing

Coding

Coded - Design and coding required

Number of Pages Required

4 page

Font styles to use
Sans Serif

Colors
ffffff
ec1f27
000000
5c5c5c
757575
b2b2b2

Requirements
Must have
• Color Scheme - should follow around our logo
• As for pages we were looking for an About, Services, Projects (gallery page) and Contact.
• Main page please include social media links and a a place so people could use coinwell to make payments
• Website should work on desktop as well as mobile platforms
Nice to have
• A Live chat feature would be nice if possible
Should not have
• Obscure Colors or Common web templates

```html
<!DOCTYPE html>
<html lang="en">
<head>
<meta charset="utf-8">
<title>Brindlecrest Roofing</title>
<link rel="stylesheet" href="https://fonts.googleapis.com/css2?family=Roboto:wght@300;400;500;700&display=swap">
<style>
:root{
  --red:#ec1f27;
  --black:#000000;
  --ink:#222222;
  --grey-dark:#5c5c5c;
  --grey:#757575;
  --grey-light:#b2b2b2;
  --white:#ffffff;
  --panel:#f3f3f3;
  --strip:#f0f1f4;
  --footer:#1b1b1b;
}
*{box-sizing:border-box;margin:0;padding:0}
html,body{width:1200px;height:2270px;overflow:hidden}
body{position:relative;font-family:'Roboto',Arial,sans-serif;color:var(--ink);background:var(--white)}
.abs{position:absolute}

/* top bar */
.topbar{left:0;top:0;width:1200px;height:43px;background:var(--black);color:var(--white);font-size:12px}
.social-dot{top:15px;width:13px;height:13px;border-radius:50%;background:var(--white)}
.social-dot.red{background:var(--red)}
.topbar-item{top:13px;display:flex;align-items:center;gap:7px}
.topbar-item svg{width:14px;height:14px}

/* header */
.header{left:0;top:43px;width:1200px;height:70px;background:var(--white)}
.brand{left:88px;top:11px;display:flex;align-items:center;gap:8px}
.brand-mark{width:16px;height:16px;background:var(--red)}
.brand-name{font-size:14px;font-weight:700;line-height:15px;color:var(--ink);letter-spacing:.5px}
.nav-link{top:24px;font-size:13px;color:var(--ink)}
.nav-link.active{color:var(--red)}
.nav-underline{left:796px;top:66px;width:56px;height:3px;background:var(--red)}

/* hero */
.hero{left:0;top:113px;width:1200px;height:457px;background:linear-gradient(180deg,#4a4038 0%,#6a5442 35%,#3c342e 70%,#2a2622 100%)}
.hero-title-small{left:136px;top:164px;font-size:30px;font-weight:400;color:var(--white)}
.hero-title{left:134px;top:196px;font-size:49px;font-weight:300;color:var(--white)}
.hero-title span{color:var(--red)}
.hero-text{left:134px;top:261px;width:330px;font-size:12px;line-height:20px;color:var(--white)}
.slider-arrow{top:210px;width:40px;height:40px;border:1.5px solid var(--white);border-radius:50%;display:flex;align-items:center;justify-content:center}
.quote-card{left:779px;top:82px;width:309px;height:298px;background:var(--white);box-shadow:0 4px 18px rgba(0,0,0,.25)}
.quote-card::before{content:"";position:absolute;left:0;top:14px;width:3px;height:28px;background:var(--red)}
.quote-title{left:22px;top:22px;font-size:17px;color:var(--grey-dark)}
.quote-field{left:22px;width:265px;height:40px;border-bottom:1px solid #e4e4e4;display:flex;align-items:center;gap:8px;font-size:11px;color:var(--grey)}
.quote-field svg{width:13px;height:13px}
.quote-field .chev{margin-left:auto}
.btn-red{background:var(--red);color:var(--white);border-radius:20px;display:flex;align-items:center;justify-content:center;font-size:13px;box-shadow:0 4px 8px rgba(236,31,39,.35)}
.quote-submit{left:15px;top:239px;width:110px;height:36px}

/* about */
.scroll-bubble{left:558px;top:528px;width:84px;height:84px;border-radius:50%;background:var(--white);display:flex;align-items:flex-start;justify-content:center;padding-top:14px}
.section-title{font-size:24px;font-weight:400;color:var(--ink)}
.about-title{left:0;top:607px;width:1200px;text-align:center}
.about-text{left:170px;top:645px;width:860px;text-align:center;font-size:11.5px;line-height:22px;color:var(--grey)}
.about-btn{left:549px;top:705px;width:112px;height:36px}

/* projects */
.projects{left:0;top:787px;width:1200px;height:661px;background:var(--panel)}
.projects-title{left:88px;top:35px}
.projects-sort{left:1000px;top:44px;font-size:12px;color:var(--ink);display:flex;align-items:center;gap:6px}
.project-tile{overflow:hidden}
.project-label{position:absolute;left:24px;bottom:20px;font-size:12px;color:var(--white)}
.tile-shade{position:absolute;left:0;right:0;bottom:0;height:60px;background:linear-gradient(180deg,rgba(0,0,0,0),rgba(0,0,0,.45))}
.project-hover{position:absolute;inset:0;background:rgba(0,0,0,.5);text-align:center;color:var(--white)}
.project-hover h3{margin-top:74px;font-size:19px;font-weight:400}
.project-hover p{margin:12px auto 0;width:300px;font-size:12px;line-height:20px}
.hover-icons{position:absolute;left:137px;top:162px;display:flex}
.hover-icon{width:32px;height:32px;border-radius:50%;display:flex;align-items:center;justify-content:center}
.hover-icon.outline{border:1.5px solid var(--white);margin-right:-4px}
.hover-icon.fill{background:var(--red);width:40px;height:40px;margin-top:-4px}

/* services */
.services-frame{left:132px;top:1505px;width:266px;height:341px;border:2px solid var(--red)}
.services-photo{left:144px;top:1518px;width:269px;height:319px;background:linear-gradient(180deg,#9fb6c8 0%,#c9d2da 40%,#e6e8ea 60%,#8c9a78 100%)}
.services-title{left:457px;top:1500px}
.service-tab{top:1551px;width:126px;height:129px;text-align:center}
.service-tab.active{border:1.5px solid #dedede;box-shadow:0 2px 6px rgba(0,0,0,.08)}
.service-icon{margin:18px auto 0;width:52px;height:52px;display:flex;align-items:center;justify-content:center}
.service-tab.active .service-icon{background:var(--red);border-radius:50%;box-shadow:0 3px 8px rgba(236,31,39,.35)}
.service-name{margin-top:16px;font-size:13px;color:var(--grey-dark)}
.service-tab.active .service-name{color:var(--ink)}
.service-num{left:455px;top:1697px;font-size:40px;font-weight:300;color:var(--grey-light)}
.service-heading{left:511px;top:1712px;font-size:19px;color:var(--ink)}
.service-text{left:507px;top:1745px;width:440px;font-size:11.5px;line-height:19px;color:var(--grey)}
.btn-outline{left:507px;top:1805px;width:112px;height:40px;border:1.5px solid #cfcfcf;border-radius:20px;display:flex;align-items:center;justify-content:center;font-size:12px;color:var(--grey-dark)}

/* partner strip */
.brand-strip{left:0;top:1909px;width:1200px;height:103px;background:var(--strip)}
.strip-name{top:40px;width:120px;text-align:center;font-size:13px;font-weight:700;line-height:14px;color:#9a9a9a}
.strip-name.dark{color:var(--ink)}

/* live chat */
.chat{left:912px;top:1744px;width:288px;height:264px;background:var(--white);box-shadow:0 2px 12px rgba(0,0,0,.2)}
.chat-head{left:0;top:0;width:288px;height:28px;background:#f0f0f0;font-size:11px;font-weight:500;color:var(--ink)}
.chat-close{left:0;top:0;width:30px;height:28px;background:var(--black);display:flex;align-items:center;justify-content:center}
.chat-head span{position:absolute;left:47px;top:8px}
.chat-avatar{left:24px;top:42px;width:42px;height:42px;border-radius:50%;background:linear-gradient(135deg,#e8c9ac,#b98460)}
.chat-hello{left:80px;top:42px;font-size:17px;color:var(--ink)}
.chat-sub{left:80px;top:66px;font-size:11px;color:var(--grey-dark)}
.chat-input{left:26px;width:230px;height:30px;border:1px solid #cfcfcf;font-size:10.5px;color:var(--grey-light);padding:9px 10px}
.chat-input.focus{border-color:#7aa6d6}
.chat-submit{left:26px;top:187px;width:74px;height:31px;background:var(--red);color:var(--white);font-size:11px;display:flex;align-items:center;justify-content:center}

/* footer */
.footer{left:0;top:2012px;width:1200px;height:215px;background:var(--footer);color:var(--white)}
.footer-head{top:36px;font-size:15px;font-weight:500}
.footer-text{font-size:11px;line-height:19px;color:#dddddd}
.footer-links{top:68px;font-size:11px;line-height:24px;color:#dddddd;list-style:none}
.footer-input{left:619px;top:117px;width:212px;height:26px;border-bottom:1px solid #777;font-size:11px;color:#aaaaaa;padding-top:6px}
.footer-input svg{position:absolute;right:10px;top:6px}
.contact-row{left:911px;display:flex;gap:12px}
.contact-row svg{flex:none;margin-top:4px}
.bottombar{left:0;top:2227px;width:1200px;height:43px;background:var(--black);color:var(--white);font-size:11px}
</style>
</head>
<body>

<!-- top bar -->
<div class="abs topbar">
  <div class="abs social-dot" style="left:88px"></div>
  <div class="abs social-dot red" style="left:112px"></div>
  <div class="abs social-dot" style="left:138px"></div>
  <div class="abs social-dot" style="left:164px"></div>
  <div class="abs topbar-item" style="left:812px">
    <svg viewBox="0 0 14 14" fill="none" stroke="#fff" stroke-width="1.2"><rect x="1" y="3" width="12" height="8"/><path d="M1 3l6 5 6-5"/></svg>info@brindlecrest-demo.net</div>
  <div class="abs topbar-item" style="left:990px">
    <svg viewBox="0 0 14 14" fill="none" stroke="#fff" stroke-width="1.2"><path d="M3 1.5l2.5 3-1.5 1.5c1 2 2 3 4 4L9.5 8.5l3 2.5-1.5 2C6 12.5 1.5 8 1 3z"/></svg>555-014-0198</div>
  <div class="abs topbar-item" style="left:1100px">
    <svg viewBox="0 0 14 14" fill="none" stroke="#fff" stroke-width="1.2"><path d="M7 13s4.5-4.5 4.5-7.5a4.5 4.5 0 0 0-9 0C2.5 8.5 7 13 7 13z"/><circle cx="7" cy="5.5" r="1.6"/></svg>Locations</div>
</div>

<!-- header -->
<header class="abs header">
  <div class="abs brand"><div class="brand-mark"></div><div class="brand-name">BRINDLECREST<br>ROOFING</div></div>
  <nav>
    <span class="abs nav-link active" style="left:806px">Home</span>
    <span class="abs nav-link" style="left:866px">About</span>
    <span class="abs nav-link" style="left:927px">Service</span>
    <span class="abs nav-link" style="left:994px">Projects</span>
    <span class="abs nav-link" style="left:1066px">Contact</span>
  </nav>
  <div class="abs nav-underline"></div>
</header>

<!-- hero -->
<section class="abs hero" role="img" aria-label="Photo of rooftops at dusk with hills behind">
  <div class="abs hero-title-small">Welcome To</div>
  <h1 class="abs hero-title">Brindlecrest <span>Roofing</span></h1>
  <p class="abs hero-text">Committed to giving you the best value when you hire our company to do any project on your home.</p>
  <div class="abs slider-arrow" style="left:24px"><svg width="12" height="12" viewBox="0 0 12 12" fill="none" stroke="#fff" stroke-width="1.5"><path d="M8 2L4 6l4 4"/></svg></div>
  <div class="abs slider-arrow" style="left:1134px"><svg width="12" height="12" viewBox="0 0 12 12" fill="none" stroke="#fff" stroke-width="1.5"><path d="M4 2l4 4-4 4"/></svg></div>

  <form class="abs quote-card">
    <div class="abs quote-title">Request Quote</div>
    <div class="abs quote-field" style="top:50px"><svg viewBox="0 0 13 13" fill="none" stroke="#757575"><circle cx="6.5" cy="4" r="2.5"/><path d="M2 12c0-3 2-4.5 4.5-4.5S11 9 11 12"/></svg>Name</div>
    <div class="abs quote-field" style="top:94px"><svg viewBox="0 0 13 13" fill="none" stroke="#757575"><path d="M3 1.5l2 3-1.3 1.3c.9 1.8 1.8 2.7 3.5 3.5L8.5 8l3 2-1.5 1.8C5.5 11.5 1.5 7.5 1 3z"/></svg>Phone no</div>
    <div class="abs quote-field" style="top:134px"><svg viewBox="0 0 13 13" fill="none" stroke="#757575"><rect x="1" y="3" width="11" height="7"/><path d="M1 3l5.5 4L12 3"/></svg>E-mail</div>
    <div class="abs quote-field" style="top:175px"><svg viewBox="0 0 13 13" fill="none" stroke="#757575"><circle cx="6.5" cy="4" r="2.5"/><path d="M2 12c0-3 2-4.5 4.5-4.5S11 9 11 12"/></svg>I'm interested in<svg class="chev" viewBox="0 0 13 13" fill="none" stroke="#5c5c5c" stroke-width="1.4"><path d="M3 5l3.5 3.5L10 5"/></svg></div>
    <div class="abs btn-red quote-submit">Sign up</div>
  </form>
</section>

<!-- about -->
<div class="abs scroll-bubble"><svg width="16" height="20" viewBox="0 0 16 20" fill="none" stroke="#222" stroke-width="1.5"><path d="M8 1v17M2 12l6 6 6-6"/></svg></div>
<h2 class="abs section-title about-title">About</h2>
<p class="abs about-text">We are a family owned, owner operated company as well as a Full-Time Professional Roofing Company.&nbsp; We have built our success by providing homeowners as well as small businesses in the entire Chicagoland and Greater Indiana area with quality work at competitive rates</p>
<div class="abs btn-red about-btn">Read More</div>

<!-- projects -->
<section class="abs projects">
  <h2 class="abs section-title projects-title">Our Projects</h2>
  <div class="abs projects-sort">Sort By Projects <svg width="10" height="10" viewBox="0 0 10 10" fill="none" stroke="#222" stroke-width="1.4"><path d="M2 3.5l3 3 3-3"/></svg></div>

  <div class="abs project-tile" style="left:88px;top:84px;width:428px;height:227px;background:linear-gradient(160deg,#8a8478,#4d4a44)" role="img" aria-label="Close-up of weathered clay roof tiles">
    <div class="tile-shade"></div><span class="project-label">Project Name</span></div>
  <div class="abs project-tile" style="left:525px;top:84px;width:286px;height:227px;background:linear-gradient(180deg,#3f6fb0 0%,#7fa3cf 45%,#b9aa92 70%,#8d8270 100%)" role="img" aria-label="Stone bell tower above a sloped roof under blue sky">
    <div class="tile-shade"></div><span class="project-label">Project Name</span></div>
  <div class="abs project-tile" style="left:822px;top:84px;width:287px;height:519px;background:linear-gradient(180deg,#1d47a8 0%,#2f5fc0 50%,#d88a52 65%,#c96a35 85%,#5a3c2c 100%)" role="img" aria-label="Orange terracotta roof with chimneys against deep blue sky">
    <div class="tile-shade"></div><span class="project-label">Project Name</span></div>
  <div class="abs project-tile" style="left:88px;top:322px;width:357px;height:281px;background:linear-gradient(180deg,#4f9ad8 0%,#8cc3ea 30%,#e6e2dc 50%,#c8c2b2 75%,#4a4a48 100%)" role="img" aria-label="White roof eave and building facade under blue sky">
    <div class="tile-shade"></div><span class="project-label">Project Name</span></div>
  <div class="abs project-tile" style="left:455px;top:322px;width:357px;height:281px;background:linear-gradient(160deg,#5d6658,#3c3430 60%,#2a2522)" role="img" aria-label="Red brick house with dark roof among misty trees">
    <div class="project-hover">
      <h3>Project Name</h3>
      <p>Lorem Ipsum is simply dummy text of the printing and typesetting industry.</p>
      <div class="hover-icons">
        <div class="hover-icon outline"><svg width="14" height="14" viewBox="0 0 14 14" fill="none" stroke="#fff" stroke-width="1.4"><path d="M6 8l2-2M5 6.5L3.5 8a2 2 0 0 0 2.8 2.8L7.8 9.3M9 7.5l1.5-1.5a2 2 0 0 0-2.8-2.8L6.2 4.7"/></svg></div>
        <div class="hover-icon fill"><svg width="14" height="14" viewBox="0 0 14 14" fill="none" stroke="#fff" stroke-width="1.6"><circle cx="6" cy="6" r="3.8"/><path d="M9 9l3 3"/></svg></div>
      </div>
    </div>
  </div>
</section>

<!-- services -->
<div class="abs services-frame"></div>
<div class="abs services-photo" role="img" aria-label="White two-storey house with balcony and grey roof"></div>
<h2 class="abs section-title services-title">Our Services</h2>

<div class="abs service-tab active" style="left:457px">
  <div class="service-icon"><svg width="26" height="22" viewBox="0 0 26 22" fill="none" stroke="#fff" stroke-width="1.6"><path d="M2 11L13 2l11 9M5 9v11h16V9M10 20v-6h6v6"/></svg></div>
  <div class="service-name">ROOFING</div>
</div>
<div class="abs service-tab" style="left:607px">
  <div class="service-icon"><svg width="22" height="24" viewBox="0 0 22 24" fill="none" stroke="#5c5c5c" stroke-width="1.4"><rect x="3" y="2" width="16" height="20"/><path d="M3 12h16M11 2v20M6 7l5 5 5-5"/></svg></div>
  <div class="service-name">SERVICE 2</div>
</div>
<div class="abs service-tab" style="left:749px">
  <div class="service-icon"><svg width="34" height="18" viewBox="0 0 34 18" fill="none" stroke="#5c5c5c" stroke-width="1.4"><path d="M2 16L10 2h22l-8 14zM8 16l8-14M14 16l8-14M20 16l8-14"/></svg></div>
  <div class="service-name">SERVICE 3</div>
</div>
<div class="abs service-tab" style="left:896px">
  <div class="service-icon"><svg width="26" height="26" viewBox="0 0 26 26" fill="none" stroke="#5c5c5c" stroke-width="1.4"><path d="M2 12L13 3l11 9M5 10v13h16V10M9 14h8M9 18h8M9 22h8"/></svg></div>
  <div class="service-name">SERVICE 4</div>
</div>

<div class="abs service-num">01</div>
<h3 class="abs service-heading">Roofing</h3>
<p class="abs service-text">Lorem Ipsum is simply dummy text of the printing and typesetting industry. Lorem Ipsum has been the industry's standard dummy text ever since the 1500s.</p>
<div class="abs btn-outline">Read More</div>

<!-- partner strip -->
<div class="abs brand-strip">
  <div class="abs strip-name" style="left:108px">BRINDLECREST<br>ROOFING</div>
  <div class="abs strip-name" style="left:279px">BRINDLECREST<br>ROOFING</div>
  <div class="abs strip-name dark" style="left:462px">BRINDLECREST<br>ROOFING</div>
  <div class="abs strip-name" style="left:645px">BRINDLECREST<br>ROOFING</div>
  <div class="abs strip-name" style="left:801px">BRINDLECREST<br>ROOFING</div>
</div>

<!-- live chat -->
<aside class="abs chat">
  <div class="abs chat-head"><div class="abs chat-close"><svg width="10" height="10" viewBox="0 0 10 10" stroke="#fff" stroke-width="1.6"><path d="M1 1l8 8M9 1l-8 8"/></svg></div><span>Live Chat</span></div>
  <div class="abs chat-avatar" role="img" aria-label="Support agent avatar"></div>
  <div class="abs chat-hello">Hello,</div>
  <div class="abs chat-sub">How may i assist you</div>
  <div class="abs chat-input focus" style="top:95px">Your Name</div>
  <div class="abs chat-input" style="top:139px">Email Address</div>
  <div class="abs chat-submit">Submit</div>
</aside>

<!-- footer -->
<footer class="abs footer">
  <h4 class="abs footer-head" style="left:88px">About</h4>
  <p class="abs footer-text" style="left:88px;top:68px;width:275px">Aenean vulputate eleifend tellus aenean leo ligula porttitor eu consequat vitae eleifend ac enim aliquam lorem ante dapibus in viverra quis feugiat a tellus phasellus viverra nulla ut metus varius laoreet quis-que rutrum.</p>

  <h4 class="abs footer-head" style="left:431px">Useful Links</h4>
  <ul class="abs footer-links" style="left:431px">
    <li>Steel Sheet Roofing</li>
    <li>Repairs &amp; Maintenance</li>
    <li>Roof Vent Installation</li>
    <li>Leaf Free Gutter Guard</li>
    <li>Gutters, Downpipes</li>
  </ul>

  <h4 class="abs footer-head" style="left:619px">Follow Us</h4>
  <p class="abs footer-text" style="left:619px;top:68px;width:225px">Subscribe to our newsletter to get latest updates and offers.</p>
  <div class="abs footer-input">Enter email<svg width="12" height="12" viewBox="0 0 12 12" fill="#ec1f27"><path d="M1 6l10-5-3 10-2-4z"/></svg></div>

  <h4 class="abs footer-head" style="left:911px">Contact information</h4>
  <div class="abs contact-row footer-text" style="top:68px"><svg width="9" height="11" viewBox="0 0 9 11" fill="#fff"><path d="M4.5 11S0 6.5 0 4a4.5 4.5 0 0 1 9 0c0 2.5-4.5 7-4.5 7z"/></svg><span>Some address line here..., area info,<br>City name, Country name.</span></div>
  <div class="abs contact-row footer-text" style="top:115px"><svg width="9" height="11" viewBox="0 0 9 11" fill="#fff"><path d="M1.5 0l2 2.5-1 1.2c.6 1.5 1.4 2.3 2.8 3l1.2-1L9 8 7.5 10C3 9.5 0 5 0 1z"/></svg><span>555-014-0198</span></div>
  <div class="abs contact-row footer-text" style="top:140px"><svg width="9" height="11" viewBox="0 0 9 11" fill="#fff"><path d="M0 3h9v6H0z"/></svg><span>info@brindlecrest-demo.net</span></div>
</footer>

<div class="abs bottombar">
  <span class="abs" style="left:90px;top:15px">Copyright 2016. All Right Reserved</span>
  <div class="abs social-dot" style="left:1012px"></div>
  <div class="abs social-dot red" style="left:1036px"></div>
  <div class="abs social-dot" style="left:1062px"></div>
  <div class="abs social-dot" style="left:1088px"></div>
</div>

</body>
</html>
```